-business card/letter head design for franchise paralegal
-business card/letter head design for franchise paralegal - Law
Professional
Franchise Paralegal
718 Pelham Lane
carlabpc@postvine.net
CarlaMBement CarlaMBement
I just notice the city and state are missing from all of my business card designs. Not sure how that happened. Full address should read "718 Pelham Lane, Linden Falls, Oregon 93127"

```html
<!DOCTYPE html>
<html lang="en">
<head>
<meta charset="utf-8">
<title>Carla Bement – Business Card</title>
<link rel="stylesheet" href="https://fonts.googleapis.com/css2?family=Open+Sans:wght@400;600&display=swap">
<style>
  :root {
    --stage: #2a2a2b;
    --green-light: #5fa520;
    --green-mid: #2f7d12;
    --green-dark: #174f07;
    --paper: #ffffff;
    --ink-blue: #1f3c9a;
    --ink-green: #3f8f1c;
    --ink-grey: #4a4a4a;
    --band-top: #2346c4;
    --band-bottom: #ffffff;
    --faint: #eef1f5;
  }
  * { margin: 0; padding: 0; box-sizing: border-box; }
  html, body { width: 1200px; height: 900px; overflow: hidden; }
  body {
    background: var(--stage);
    font-family: "Open Sans", Arial, sans-serif;
    position: relative;
  }
  .card {
    position: absolute;
    width: 560px;
    height: 320px;
    overflow: hidden;
    box-shadow: 0 10px 30px rgba(0,0,0,.5);
  }
  /* Back card */
  .card-back {
    left: 90px; top: 110px;
    background: radial-gradient(ellipse at 45% 35%, var(--green-light) 0%, var(--green-mid) 45%, var(--green-dark) 100%);
    color: var(--paper);
    text-align: center;
  }
  .card-back .mark {
    display: flex; align-items: center; justify-content: center; gap: 14px;
    margin-top: 110px;
  }
  .mark-dot {
    width: 40px; height: 40px; border-radius: 50%;
    border: 3px solid currentColor;
    flex: none;
  }
  .card-back .brand-name {
    font-size: 34px; font-weight: 600; letter-spacing: 1px;
  }
  .card-back .tagline {
    margin-top: 34px;
    font-size: 14px; letter-spacing: 2.5px;
  }
  /* Front card */
  .card-front {
    left: 550px; top: 470px;
    background: var(--paper);
  }
  .watermark {
    position: absolute; left: 20px; top: 40px;
    width: 300px; height: 300px; border-radius: 50%;
    border: 22px solid var(--faint);
  }
  .band {
    position: absolute; right: 90px; top: 0;
    width: 96px; height: 80px;
    background: linear-gradient(to bottom, var(--band-top), var(--band-bottom));
  }
  .front-mark {
    position: absolute; right: 40px; top: 88px;
    display: flex; align-items: center; gap: 10px;
    color: var(--ink-blue);
  }
  .front-mark .mark-dot { width: 30px; height: 30px; border-width: 2px; }
  .front-mark .brand-name { font-size: 24px; font-weight: 600; }
  .contact {
    position: absolute; left: 40px; bottom: 28px;
    color: var(--ink-grey); font-size: 14px; line-height: 1.5;
  }
  .contact .person { color: var(--ink-blue); font-size: 21px; font-weight: 600; line-height: 1.2; }
  .contact .role { color: var(--ink-green); font-size: 15px; margin-bottom: 8px; }
  .contact .line { display: flex; align-items: center; gap: 8px; }
  .contact .address { margin-bottom: 8px; }
  .contact svg { width: 14px; height: 14px; fill: var(--ink-green); flex: none; }
</style>
</head>
<body>
  <section class="card card-back">
    <div class="mark">
      <span class="mark-dot"></span>
      <span class="brand-name">Carla Bement</span>
    </div>
    <p class="tagline">Restaurant Franchise Administrator</p>
  </section>

  <section class="card card-front">
    <div class="watermark"></div>
    <div class="band"></div>
    <div class="front-mark">
      <span class="mark-dot"></span>
      <span class="brand-name">Carla Bement</span>
    </div>
    <div class="contact">
      <p class="person">Carla Bement</p>
      <p class="role">Franchise Paralegal</p>
      <p class="address">718 Pelham Lane<br>Linden Falls, Oregon 93127</p>
      <p class="line">
        <svg viewBox="0 0 24 24" aria-hidden="true"><path d="M6.6 10.8a15.1 15.1 0 0 0 6.6 6.6l2.2-2.2c.3-.3.7-.4 1-.2 1.1.4 2.3.6 3.6.6.6 0 1 .4 1 1V20c0 .6-.4 1-1 1A17 17 0 0 1 3 4c0-.6.4-1 1-1h3.5c.6 0 1 .4 1 1 0 1.3.2 2.5.6 3.6.1.3 0 .7-.2 1z"/></svg>
        555-214-0148
      </p>
      <p class="line">
        <svg viewBox="0 0 24 24" aria-hidden="true"><path d="M2 5h20v14H2z M2 5l10 8 10-8" fill="none" stroke="#3f8f1c" stroke-width="2"/></svg>
        carlabpc@postvine.net
      </p>
    </div>
  </section>
</body>
</html>
```